Brochure Design*

We are seeking a simple but powerful brochure design for our new company that uses electrostatic sprayers for the treatment and prevention of Covid 19 for businesses throughout the Southeast. The current brochure has too many photos and very distracting, i personally do not like anything about the brochure. Our sister company Harlow Print Supply was founded in 1983. Our company HPS Services LLC website is www.hpsvx.com
Updates

We need a few more days to receive feedback from our employees. Thank You

Target Market(s)

Business owners

Font styles to use
Serif
Sans Serif

Requirements
Must have
• A call for action brochure, simple while delivering a strong message
Should not have
• CLUTTER,

```html
<!DOCTYPE html>
<html lang="en">
<head>
<meta charset="utf-8">
<title>HPS Services – Disinfect Your Institution</title>
<link href="https://fonts.googleapis.com/css2?family=Lato:wght@300;400;700;900&family=Noto+Sans:wght@300;800&display=swap" rel="stylesheet">
<style>
  :root{
    --ink:#111111;
    --black:#050505;
    --green:#3cb54a;
    --green-deep:#2e9a3c;
    --green-light:#5fcc6c;
    --green-dark:#3f8f4f;
    --paper:#f2f2f2;
    --stage:#e6ecee;
    --photo-a:#e9ecea;
    --photo-b:#9aa3a0;
  }
  *{margin:0;padding:0;box-sizing:border-box}
  html,body{width:1200px;height:900px;overflow:hidden;background:var(--stage)}
  .flyer{
    position:absolute;left:300px;top:26px;width:600px;height:848px;
    background:var(--paper);overflow:hidden;
    font-family:"Lato",sans-serif;color:var(--ink);
    box-shadow:0 6px 24px rgba(0,0,0,.12);
  }
  .flyer-art{position:absolute;inset:0}
  .brand{
    position:absolute;left:32px;top:38px;
    font-family:"Lato",sans-serif;font-weight:900;font-size:24px;
    color:var(--green-light);letter-spacing:.5px;
  }
  .headline{position:absolute;left:40px;top:430px;line-height:1}
  .headline-strong{display:block;font-family:"Noto Sans",sans-serif;font-weight:800;font-size:46px}
  .headline-light{display:block;font-family:"Noto Sans",sans-serif;font-weight:300;font-size:46px;margin-top:2px}
  .intro{
    position:absolute;left:40px;top:540px;width:330px;
    padding-left:14px;border-left:4px solid var(--green);
    font-size:13px;line-height:1.45;
  }
  .call{position:absolute;left:40px;top:626px}
  .call-label{display:block;font-weight:700;font-size:17px}
  .call-number{display:block;font-weight:900;font-size:32px;letter-spacing:.5px}
  .sectors{
    position:absolute;right:36px;top:470px;list-style:none;text-align:right;
    font-weight:900;font-size:17px;line-height:1.95;
  }
  .address{
    position:absolute;left:40px;top:792px;color:#fff;font-size:12.5px;line-height:1.4;
  }
  .website{
    position:absolute;right:28px;top:806px;color:#fff;font-size:17px;letter-spacing:.3px;
  }
</style>
</head>
<body>
<main class="flyer">
  <svg class="flyer-art" viewBox="0 0 600 848" width="600" height="848">
    <rect class="hero-bg" x="0" y="0" width="600" height="470" fill="var(--green)"/>
    <path class="hero-shade" d="M0,330 C120,300 220,360 330,340 C430,320 520,260 600,250 L600,470 L0,470 Z" fill="var(--green-deep)"/>
    <path class="top-band" d="M0,0 H600 V55 L0,120 Z" fill="var(--black)"/>
    <g role="img" aria-label="Photo of a technician in a white protective suit and respirator holding an electrostatic disinfection sprayer">
      <path d="M250,190 C270,120 330,80 380,70 C440,60 520,90 560,140 L580,420 L260,420 Z" fill="url(#photoTone)"/>
      <path d="M90,230 C110,200 170,190 210,205 L300,240 L260,400 L120,380 Z" fill="url(#deviceTone)"/>
    </g>
    <path class="content-wave" d="M0,470 C90,420 160,390 260,400 C360,410 420,330 490,300 C540,280 580,275 600,272 L600,848 L0,848 Z" fill="var(--paper)"/>
    <ellipse class="seal" cx="210" cy="750" rx="78" ry="44" fill="none" stroke="#9a9a9a" stroke-width="2"/>
    <ellipse cx="210" cy="750" rx="72" ry="38" fill="none" stroke="#b5b5b5" stroke-width="1"/>
    <path class="footer-band" d="M0,790 L600,770 V848 H0 Z" fill="var(--green-light)"/>
    <path class="footer-block" d="M370,778 L600,770 V848 H370 Z" fill="var(--green-dark)"/>
    <defs>
      <linearGradient id="photoTone" x1="0" y1="0" x2="1" y2="1">
        <stop offset="0" stop-color="var(--photo-a)"/>
        <stop offset="1" stop-color="var(--photo-b)"/>
      </linearGradient>
      <linearGradient id="deviceTone" x1="0" y1="0" x2="1" y2="1">
        <stop offset="0" stop-color="#3a3a3a"/>
        <stop offset="1" stop-color="#111"/>
      </linearGradient>
    </defs>
  </svg>

  <div class="brand">HPS Services, LLC</div>

  <h1 class="headline">
    <span class="headline-strong">Disinfect</span>
    <span class="headline-light">Your Institution</span>
  </h1>

  <p class="intro">HPS Services NC offers disinfection services against the corona virus and other pathogens. Protect your clients, your staff and yourself.</p>

  <div class="call">
    <span class="call-label">Call Now:</span>
    <span class="call-number">1-800-555-0142</span>
  </div>

  <ul class="sectors">
    <li>Offices/ Banks</li>
    <li>Bars/ Restaurants</li>
    <li>Gym/ Sports Facilities</li>
    <li>Medical/ Hospitals</li>
    <li>Schools/ Daycares</li>
    <li>Data/ Call Centers</li>
  </ul>

  <address class="address">410 Linden Row<br>Cary, North Carolina 27511</address>
  <div class="website">hpsvxnc.com/</div>
</main>
</body>
</html>
```